I need a book cover for my book titled Sunny Porch! The subtitle is Quiet Orchard Days and the the author is Marisol Dunleavy. I want the attached photo included on the cover, plus the words "I never met a chicken wing I didn't like!" The book size is 5.06 x 7.81 in. and is 146 pages. For the color scheme, I like a chocolate brown cover with aqua blue letters. (Please note that you don't have to use these colors. Feel free to use this color scheme or whatever you colors you like!)

• Please include my photo for the back cover, along with this text:

Sunny Porch! I was tired of being tired! I was tired of acid reflux, body stiffness, and being overweight. To make matters worse, I suffered from back pain, constipation, leg pain, and lack of sleep. If you are tired of looking to medical test for your answers, this is the book for you. The key was the day I decided to make “me” a priority by being #1 on my “to-do” list.

Our healthcare system seems to be more concerned about treating illness than they are about preventing it; which is why we have so many problems with our health and wellness. That’s why I’m going to give you insights into nutrition, health care, and the pharmaceutical industry.

I’m also going to give you some insights into exercise, supplements, detoxing and essential oils; as well as what goes into your grocery cart and the foods you feed your family.

Because you’re reading this I know you’re ready to live your best life, Sunny Porch! is for you.

Here’s to a healthy you!

Here's a brief bio about the author for the back cover:

Marisol lives in Chicago with her husband, Dr. Wendell, and has three adult children. She is probably one of the most private people you will meet – BUT HAD to tell her story!

```html
<!DOCTYPE html>
<html lang="en">
<head>
<meta charset="utf-8">
<title>Sunny Porch! – Back Cover</title>
<link href="https://fonts.googleapis.com/css2?family=Roboto:wght@700&display=swap" rel="stylesheet">
<style>
  :root {
    --panel-main: #5d4b3b;
    --panel-side: #4b3319;
    --aqua: #1aa4e8;
    --photo-warm: #8a6238;
    --photo-dark: #2b1e14;
  }
  html, body {
    margin: 0;
    padding: 0;
    width: 777px;
    height: 1200px;
    overflow: hidden;
  }
  .back-cover {
    position: relative;
    width: 777px;
    height: 1200px;
    display: flex;
    font-family: "Roboto", Arial, sans-serif;
    font-weight: 700;
    color: var(--aqua);
    letter-spacing: -0.6px;
  }
  .blurb-panel {
    width: 546px;
    height: 100%;
    background: var(--panel-main);
    box-sizing: border-box;
    padding: 113px 48px 0 65px;
  }
  .blurb-panel p {
    margin: 0 0 30px;
    font-size: 24.5px;
    line-height: 30px;
  }
  .author-panel {
    flex: 1;
    height: 100%;
    background: var(--panel-side);
    position: relative;
  }
  .author-photo {
    position: absolute;
    left: 34px;
    top: 302px;
    width: 161px;
    height: 283px;
    background: linear-gradient(160deg, var(--photo-warm) 0%, #6b4a2c 45%, var(--photo-dark) 100%);
  }
  .author-bio {
    position: absolute;
    left: 35px;
    top: 608px;
    width: 190px;
    margin: 0;
    font-size: 20px;
    line-height: 25.5px;
    letter-spacing: -0.7px;
  }
</style>
</head>
<body>
  <div class="back-cover">
    <section class="blurb-panel">
      <p>Sunny Porch! I was tired of being tired! I was tired of acid reflux, body stiffness, and being overweight. To make matters worse, I suffered from back pain, constipation, leg pain, and lack of sleep. If you are tired of looking to medical test for your answers, this is the book for you. The key was the day I decided to make “me” a priority by being #1 on my “to-do” list.</p>
      <p>Our healthcare system seems to be more concerned about treating illness than they are about preventing it; which is why we have so many problems with our health and wellness. That’s why I’m going to give you insights into nutrition, health care, and the pharmaceutical industry.</p>
      <p>I’m also going to give you some insights into exercise, supplements, detoxing and essential oils; as well as what goes into your grocery cart and the foods you feed your family.</p>
      <p>Because you’re reading this I know you’re ready to live your best life, Sunny Porch! is for you.</p>
      <p>Here’s to a healthy you!</p>
    </section>
    <aside class="author-panel">
      <div class="author-photo" role="img" aria-label="Portrait photo of the author"></div>
      <p class="author-bio">Marisol lives in Chicago with her husband, Dr. Wendell, and has three adult children. She is probably one of the most private people you will meet – BUT HAD to tell her story!</p>
    </aside>
  </div>
</body>
</html>
```